Price Package PDF - 2 page PDF of stylized price packages for property management firm

Looking for a 2 x A4 page PDF for our two price packages.
I would like this to be in similar style to our website www.harbourlanerentals.com.au
I have attached an example. But would like mine to be a little more stylish and modern, preferably using design similar to our website.
Words and images also attached

Target Market(s)

investment property owners, male and female, aged 30-60

Industry/Entity Type

Real Estate

Font styles to use
Sans Serif

Requirements
Must have
• split two packages onto seperate A4 pages (See example file attached)
• Contact info:
• Website: www.harbourlanerentals.com.au
• email: info@harbourlanerentals.com.au
• Phone: Tom Radley 0417 562 903, Larisa Okonjo 0409 317 648
• Office Address: Suite 7, 12-14 Wattle Parade, Curl Curl NSW 2096
Nice to have
• I would like to use any of the pictures provided or images of modern residential property interior or of Sydney's Northern Beaches.

```html
<!DOCTYPE html>
<html lang="en">
<head>
<meta charset="utf-8">
<title>Harbour Lane Rentals – Price Packages</title>
<link rel="stylesheet" href="https://fonts.googleapis.com/css2?family=Jost:wght@300;400;500&display=swap">
<style>
:root{
  --bg:#2b2b2b;
  --teal:#1f8c9c;
  --teal-dark:#16707f;
  --teal-light:#5fb8c4;
  --row-label:#cfe2e7;
  --row-value:#e4eff2;
  --paper:#f4f7f8;
  --ink:#2a3a40;
  --white:#ffffff;
}
*{box-sizing:border-box;margin:0;padding:0}
html,body{width:1200px;height:864px;overflow:hidden}
body{background:var(--bg);font-family:'Jost',sans-serif;color:var(--ink);position:relative}
.page{position:absolute;top:45px;width:547px;height:773px;background:var(--paper);overflow:hidden}
.page--front{left:37px}
.page--back{left:616px}
.hero{position:absolute;left:0;top:0;width:547px;height:372px}
.hero--building{background:linear-gradient(180deg,#3f8fc9 0%,#8fc0e0 28%,#7a8a86 48%,#4f6b45 72%,#5d6660 100%)}
.hero--harbour{background:linear-gradient(180deg,#2f86c6 0%,#6fb0de 30%,#9a8a6a 40%,#1d7fb0 50%,#1566a0 100%)}
.brand{position:absolute;right:28px;top:50px;font-weight:500;font-size:22px;color:var(--white);letter-spacing:.2px}
.headline{position:absolute;left:0;width:480px;top:270px;text-align:center;font-weight:300;font-size:32px;line-height:42px;color:var(--white)}
.band{position:absolute;left:0;top:358px}
.band-title{position:absolute;left:38px;top:363px;font-size:21px;color:var(--white);font-weight:400}
.includes-title{position:absolute;left:33px;top:418px;font-size:20px;color:var(--teal-dark)}
.includes{position:absolute;left:33px;top:452px;list-style:none;width:265px}
.includes li{position:relative;padding-left:20px;font-size:11px;line-height:13px;margin-bottom:4.3px}
.includes li svg{position:absolute;left:0;top:2px}
.table-tab{position:absolute;left:298px;top:415px}
.table-title{position:absolute;left:338px;top:419px;font-size:18px;color:var(--white)}
.price-table{position:absolute;left:298px;top:454px;width:249px}
.row{display:flex;height:24px;margin-bottom:2.6px}
.row .label{width:125px;background:var(--row-label);font-size:12px;padding-left:10px;display:flex;align-items:center;line-height:12px}
.row .value{flex:1;background:var(--row-value);font-size:12.5px;padding-left:10px;display:flex;flex-direction:column;justify-content:center;line-height:12px;margin-left:3px}
.row .value small{font-size:7.5px;line-height:8px}
.row--tall{height:32px}
.value--big{font-size:15px!important}
.value--tiny{font-size:8.5px!important;line-height:9px!important}
.contact-tab{position:absolute;left:298px;top:650px;width:76px;height:15px;background:var(--teal);color:var(--white);font-size:10px;padding-left:8px;line-height:15px}
.contact-band{position:absolute;left:272px;top:666px}
.contact-lines{position:absolute;left:300px;top:670px;width:240px;color:var(--white);font-size:15px;line-height:22px;text-align:right}
.contact-lines b{font-weight:500;font-size:17px}
.phone-icon{position:absolute;left:294px;top:673px}
.email{position:absolute;right:10px;top:724px;font-size:13px;display:flex;align-items:center;gap:6px}
.footer{position:absolute;left:0;top:743px;width:547px;height:30px}
.footer-address{position:absolute;left:28px;top:750px;font-size:11px;color:var(--white);display:flex;align-items:center;gap:6px}
.footer-web{position:absolute;right:12px;top:750px;font-size:12px;color:var(--white);display:flex;align-items:center;gap:6px}
</style>
</head>
<body>

<!-- FRONT PAGE -->
<section class="page page--front">
  <div class="hero hero--building" role="img" aria-label="Photo of modern terraced townhouses with landscaped gardens under a blue sky"></div>
  <div class="brand">HARBOUR LANE RENTALS</div>
  <h1 class="headline">PROPERTY MANAGEMENT<br>DONE RIGHT!</h1>

  <svg class="band" width="547" height="48" viewBox="0 0 547 48"><polygon points="360,0 547,0 547,16 372,16" fill="var(--teal-light)"/><polygon points="0,6 355,6 385,48 0,48" fill="var(--teal)"/></svg>
  <div class="band-title">All Inclusive Package:</div>

  <div class="includes-title">Includes:</div>
  <ul class="includes">
    <li><svg width="11" height="9"><path d="M1 5l3 3 6-7" stroke="var(--teal)" stroke-width="1.6" fill="none"/></svg>Securing Tenant</li>
    <li><svg width="11" height="9"><path d="M1 5l3 3 6-7" stroke="var(--teal)" stroke-width="1.6" fill="none"/></svg>Reference/Database Checking</li>
    <li><svg width="11" height="9"><path d="M1 5l3 3 6-7" stroke="var(--teal)" stroke-width="1.6" fill="none"/></svg>Lease Preparation and Signing</li>
    <li><svg width="11" height="9"><path d="M1 5l3 3 6-7" stroke="var(--teal)" stroke-width="1.6" fill="none"/></svg>Direct Debit rent collection</li>
    <li><svg width="11" height="9"><path d="M1 5l3 3 6-7" stroke="var(--teal)" stroke-width="1.6" fill="none"/></svg>Zero arrears policy management</li>
    <li><svg width="11" height="9"><path d="M1 5l3 3 6-7" stroke="var(--teal)" stroke-width="1.6" fill="none"/></svg>Payment of Rates and levies</li>
    <li><svg width="11" height="9"><path d="M1 5l3 3 6-7" stroke="var(--teal)" stroke-width="1.6" fill="none"/></svg>Insurance management</li>
    <li><svg width="11" height="9"><path d="M1 5l3 3 6-7" stroke="var(--teal)" stroke-width="1.6" fill="none"/></svg>Coordination or all repairs and maintenance</li>
    <li><svg width="11" height="9"><path d="M1 5l3 3 6-7" stroke="var(--teal)" stroke-width="1.6" fill="none"/></svg>Regular rent reviews and renewals</li>
    <li><svg width="11" height="9"><path d="M1 5l3 3 6-7" stroke="var(--teal)" stroke-width="1.6" fill="none"/></svg>Detailed ingoing, ongoing and outgoing inspections with photos and videos – viewable through your personal Landlord portal</li>
    <li><svg width="11" height="9"><path d="M1 5l3 3 6-7" stroke="var(--teal)" stroke-width="1.6" fill="none"/></svg>Bond management – lodging and refunding</li>
    <li><svg width="11" height="9"><path d="M1 5l3 3 6-7" stroke="var(--teal)" stroke-width="1.6" fill="none"/></svg>Electronic monthly and EOFY statements</li>
    <li><svg width="11" height="9"><path d="M1 5l3 3 6-7" stroke="var(--teal)" stroke-width="1.6" fill="none"/></svg>Annual scheduled maintenance report</li>
    <li><svg width="11" height="9"><path d="M1 5l3 3 6-7" stroke="var(--teal)" stroke-width="1.6" fill="none"/></svg>Regulation/compliance management</li>
    <li><svg width="11" height="9"><path d="M1 5l3 3 6-7" stroke="var(--teal)" stroke-width="1.6" fill="none"/></svg>Tribunal Representation</li>
  </ul>

  <svg class="table-tab" width="249" height="31" viewBox="0 0 249 31"><polygon points="14,0 249,0 249,31 0,31" fill="var(--teal)"/></svg>
  <div class="table-title">All Inclusive Package:</div>
  <div class="price-table">
    <div class="row row--tall"><div class="label">Management Rate:</div><div class="value"><span class="value--big">10% + GST</span><small>of rental income</small></div></div>
    <div class="row"><div class="label">Letting Fee:</div><div class="value">No Charge</div></div>
    <div class="row"><div class="label">Advertising:</div><div class="value">No Charge</div></div>
    <div class="row row--tall"><div class="label">Professional<br>Photography:</div><div class="value"><span>$199 (inc GST)</span><small>4 x Photos</small></div></div>
    <div class="row"><div class="label">Statements:</div><div class="value">No Charge</div></div>
    <div class="row"><div class="label">Lease Preperation:</div><div class="value">No Charge</div></div>
    <div class="row"><div class="label">Renewal Fees:</div><div class="value">No Charge</div></div>
  </div>

  <div class="contact-tab">Contact Us</div>
  <svg class="contact-band" width="275" height="52" viewBox="0 0 275 52"><polygon points="22,0 275,0 275,52 0,52" fill="var(--teal)"/></svg>
  <svg class="phone-icon" width="18" height="18" viewBox="0 0 18 18"><circle cx="9" cy="9" r="8" fill="none" stroke="#fff" stroke-width="1.2"/><path d="M6 5l2 2-1 1c.5 1.2 1.3 2 2.5 2.5l1-1 2 2-1.2 1.2C8.5 12.5 5.5 9.5 5 6.2z" fill="#fff"/></svg>
  <div class="contact-lines">Tom Radley <b>0417 562 903</b><br>Larisa Okonjo <b>0409 317 648</b></div>
  <div class="email"><svg width="13" height="9"><rect x=".5" y=".5" width="12" height="8" fill="none" stroke="var(--teal)"/><path d="M.5 .5l6 4.5 6-4.5" fill="none" stroke="var(--teal)"/></svg>info@harbourlanerentals.com.au</div>

  <svg class="footer" width="547" height="30" viewBox="0 0 547 30"><rect width="547" height="30" fill="var(--teal-dark)"/><polygon points="300,0 547,0 547,30 285,30" fill="var(--teal)"/></svg>
  <div class="footer-address"><svg width="9" height="13"><path d="M4.5 12S0 7 0 4.5a4.5 4.5 0 019 0C9 7 4.5 12 4.5 12z" fill="#fff"/><circle cx="4.5" cy="4.5" r="1.6" fill="var(--teal-dark)"/></svg>Suite 7, 12-14 Wattle Parade, Curl Curl NSW 2096</div>
  <div class="footer-web"><svg width="12" height="12"><circle cx="6" cy="6" r="5.3" fill="none" stroke="#fff"/><ellipse cx="6" cy="6" rx="2.3" ry="5.3" fill="none" stroke="#fff"/><path d="M.7 6h10.6" stroke="#fff"/></svg>www.harbourlanerentals.com.au</div>
</section>

<!-- BACK PAGE -->
<section class="page page--back">
  <div class="hero hero--harbour" role="img" aria-label="Photo of a sunny harbour with moored boats, a motor boat and waterfront buildings"></div>
  <div class="brand">HARBOUR LANE RENTALS</div>

  <svg class="band" width="547" height="48" viewBox="0 0 547 48"><polygon points="360,0 547,0 547,16 372,16" fill="var(--teal-light)"/><polygon points="0,6 395,6 425,48 0,48" fill="var(--teal)"/></svg>
  <div class="band-title">Lease and Management Package:</div>

  <div class="includes-title">Includes:</div>
  <ul class="includes">
    <li><svg width="11" height="9"><path d="M1 5l3 3 6-7" stroke="var(--teal)" stroke-width="1.6" fill="none"/></svg>Securing Tenant</li>
    <li><svg width="11" height="9"><path d="M1 5l3 3 6-7" stroke="var(--teal)" stroke-width="1.6" fill="none"/></svg>Reference/Database Checking</li>
    <li><svg width="11" height="9"><path d="M1 5l3 3 6-7" stroke="var(--teal)" stroke-width="1.6" fill="none"/></svg>Lease Preparation and Signing</li>
    <li><svg width="11" height="9"><path d="M1 5l3 3 6-7" stroke="var(--teal)" stroke-width="1.6" fill="none"/></svg>Direct Debit rent collection</li>
    <li><svg width="11" height="9"><path d="M1 5l3 3 6-7" stroke="var(--teal)" stroke-width="1.6" fill="none"/></svg>Zero arrears policy management</li>
    <li><svg width="11" height="9"><path d="M1 5l3 3 6-7" stroke="var(--teal)" stroke-width="1.6" fill="none"/></svg>Payment of Rates and levies</li>
    <li><svg width="11" height="9"><path d="M1 5l3 3 6-7" stroke="var(--teal)" stroke-width="1.6" fill="none"/></svg>Insurance management</li>
    <li><svg width="11" height="9"><path d="M1 5l3 3 6-7" stroke="var(--teal)" stroke-width="1.6" fill="none"/></svg>Coordination or all repairs and maintenance</li>
    <li><svg width="11" height="9"><path d="M1 5l3 3 6-7" stroke="var(--teal)" stroke-width="1.6" fill="none"/></svg>Regular rent reviews and renewals</li>
    <li><svg width="11" height="9"><path d="M1 5l3 3 6-7" stroke="var(--teal)" stroke-width="1.6" fill="none"/></svg>Detailed ingoing, ongoing and outgoing inspections with photos and videos – viewable through your personal Landlord portal</li>
    <li><svg width="11" height="9"><path d="M1 5l3 3 6-7" stroke="var(--teal)" stroke-width="1.6" fill="none"/></svg>Bond management – lodging and refunding</li>
    <li><svg width="11" height="9"><path d="M1 5l3 3 6-7" stroke="var(--teal)" stroke-width="1.6" fill="none"/></svg>Electronic monthly and EOFY statements</li>
    <li><svg width="11" height="9"><path d="M1 5l3 3 6-7" stroke="var(--teal)" stroke-width="1.6" fill="none"/></svg>Annual scheduled maintenance report</li>
    <li><svg width="11" height="9"><path d="M1 5l3 3 6-7" stroke="var(--teal)" stroke-width="1.6" fill="none"/></svg>Regulation/compliance management</li>
    <li><svg width="11" height="9"><path d="M1 5l3 3 6-7" stroke="var(--teal)" stroke-width="1.6" fill="none"/></svg>Tribunal Representation</li>
  </ul>

  <svg class="table-tab" width="249" height="31" viewBox="0 0 249 31"><polygon points="14,0 249,0 249,31 0,31" fill="var(--teal)"/></svg>
  <div class="table-title">All Inclusive Package:</div>
  <div class="price-table">
    <div class="row row--tall"><div class="label">Management Rate:</div><div class="value"><span class="value--big">6% + GST</span><small>of rental income</small></div></div>
    <div class="row"><div class="label">Letting Fee:</div><div class="value"><span class="value--tiny">1 weeks rent +GST<br>6 or 12 month lease</span></div></div>
    <div class="row"><div class="label">Advertising:</div><div class="value">$350 (Inc GST)</div></div>
    <div class="row row--tall"><div class="label">Professional<br>Photography:</div><div class="value"><span>$199 (inc GST)</span><small>4 x Photos</small></div></div>
    <div class="row"><div class="label">Statements:</div><div class="value">$5.00 Per month</div></div>
    <div class="row"><div class="label">Lease Preparation:</div><div class="value">No Charge</div></div>
    <div class="row"><div class="label">Renewal Fees:</div><div class="value">½ Weeks Rent +GST</div></div>
  </div>

  <div class="contact-tab">Contact Us</div>
  <svg class="contact-band" width="275" height="52" viewBox="0 0 275 52"><polygon points="22,0 275,0 275,52 0,52" fill="var(--teal)"/></svg>
  <svg class="phone-icon" width="18" height="18" viewBox="0 0 18 18"><circle cx="9" cy="9" r="8" fill="none" stroke="#fff" stroke-width="1.2"/><path d="M6 5l2 2-1 1c.5 1.2 1.3 2 2.5 2.5l1-1 2 2-1.2 1.2C8.5 12.5 5.5 9.5 5 6.2z" fill="#fff"/></svg>
  <div class="contact-lines">Tom Radley <b>0417 562 903</b><br>Larisa Okonjo <b>0409 317 648</b></div>
  <div class="email"><svg width="13" height="9"><rect x=".5" y=".5" width="12" height="8" fill="none" stroke="var(--teal)"/><path d="M.5 .5l6 4.5 6-4.5" fill="none" stroke="var(--teal)"/></svg>info@harbourlanerentals.com.au</div>

  <svg class="footer" width="547" height="30" viewBox="0 0 547 30"><rect width="547" height="30" fill="var(--teal-dark)"/><polygon points="300,0 547,0 547,30 285,30" fill="var(--teal)"/></svg>
  <div class="footer-address"><svg width="9" height="13"><path d="M4.5 12S0 7 0 4.5a4.5 4.5 0 019 0C9 7 4.5 12 4.5 12z" fill="#fff"/><circle cx="4.5" cy="4.5" r="1.6" fill="var(--teal-dark)"/></svg>Suite 7, 12-14 Wattle Parade, Curl Curl NSW 2096</div>
  <div class="footer-web"><svg width="12" height="12"><circle cx="6" cy="6" r="5.3" fill="none" stroke="#fff"/><ellipse cx="6" cy="6" rx="2.3" ry="5.3" fill="none" stroke="#fff"/><path d="M.7 6h10.6" stroke="#fff"/></svg>www.harbourlanerentals.com.au</div>
</section>

</body>
</html>
```